ultra-minimalist business card

front (black background, matte):

tarik b. hosseny
writer | photographer
get@tarikhosseny.com

back (white background, matte):

a picture speaks a thousand words;
a word draws a thousand pictures.

www.tarikhosseny.com

all text should be small (white or silver - as long as it shows against the black - on the front; black or gray - as long as it shows against the white - on the back).

feel free to get creative in terms of arrangement, alignment, and font type, but remember, the overall style is minimalist, so nothing too fancy, please.

thanks.

```html
<!DOCTYPE html>
<html lang="en">
<head>
<meta charset="utf-8">
<title>tarik b. hosseny — business card</title>
<link rel="stylesheet" href="https://fonts.googleapis.com/css2?family=Poppins:wght@300;400;500;600&display=swap">
<style>
  :root {
    --canvas: #e4e2df;
    --card-white: #f4f4f4;
    --card-black: #2b2829;
    --ink: #1e1c1d;
    --ink-soft: #55514f;
    --silver: #e9e9e9;
    --silver-dim: #a9a6a5;
    --rule-dark: #1b191a;
    --rule-light: #f2f2f2;
  }
  * { margin: 0; padding: 0; box-sizing: border-box; }
  html, body {
    width: 1200px;
    height: 900px;
    overflow: hidden;
    background: var(--canvas);
    font-family: "Poppins", sans-serif;
  }
  .canvas {
    position: relative;
    width: 1200px;
    height: 900px;
  }
  .card {
    position: absolute;
    left: 290px;
    width: 620px;
    height: 354px;
    overflow: hidden;
    box-shadow: 0 10px 28px rgba(0, 0, 0, 0.18);
  }

  /* back side */
  .card--back {
    top: 70px;
    background: var(--card-white);
  }
  .card--back .rule {
    position: absolute;
    width: 6px;
    background: var(--rule-dark);
  }
  .card--back .rule--upper { left: 248px; top: 0; height: 150px; }
  .card--back .rule--lower { left: 500px; top: 78px; bottom: 0; }
  .quote {
    position: absolute;
    left: 40px;
    top: 222px;
    font-weight: 600;
    font-size: 19px;
    line-height: 25px;
    letter-spacing: 0.2px;
    color: var(--ink);
  }
  .card--back .website {
    position: absolute;
    left: 40px;
    top: 300px;
    font-weight: 400;
    font-size: 14px;
    letter-spacing: 0.6px;
    color: var(--ink-soft);
  }

  /* front side */
  .card--front {
    top: 476px;
    background: var(--card-black);
  }
  .card--front .rule {
    position: absolute;
    left: 184px;
    top: 0;
    bottom: 0;
    width: 5px;
    background: var(--rule-light);
  }
  .name {
    position: absolute;
    top: 150px;
    font-weight: 500;
    font-size: 52px;
    line-height: 1;
    letter-spacing: -0.5px;
    color: var(--silver);
  }
  .name--first { right: calc(620px - 176px); }
  .name--rest { left: 198px; top: 104px; }
  .role {
    position: absolute;
    left: 198px;
    width: 272px;
    top: 164px;
    text-align: right;
    font-weight: 300;
    font-size: 15px;
    letter-spacing: 1px;
    color: var(--silver-dim);
  }
  .email {
    position: absolute;
    right: 44px;
    bottom: 34px;
    font-weight: 300;
    font-size: 16px;
    letter-spacing: 0.8px;
    color: var(--silver-dim);
  }
  .card--front .website {
    position: absolute;
    right: -68px;
    top: 120px;
    transform: rotate(90deg);
    font-weight: 300;
    font-size: 13px;
    letter-spacing: 1px;
    color: var(--silver-dim);
  }
</style>
</head>
<body>
<main class="canvas">
  <section class="card card--back" aria-label="back of card">
    <span class="rule rule--upper"></span>
    <span class="rule rule--lower"></span>
    <p class="quote">a picture speaks a thousand words;<br>a word draws a thousand pictures.</p>
    <p class="website">www.tarikhosseny.com</p>
  </section>

  <section class="card card--front" aria-label="front of card">
    <span class="rule"></span>
    <h1 class="name name--first">tarik</h1>
    <p class="name name--rest">b. hosseny</p>
    <p class="role">writer | photographer</p>
    <p class="website">www.tarikhosseny.com</p>
    <p class="email">get@tarikhosseny.com</p>
  </section>
</main>
</body>
</html>
```